Flyer needed For the Council for Stewardship of Public Works

With an increasing need for professional staffing in our design and construction industry it is important for organizations to be able to attract, support, and retain people of all genders. With the increase of women entering the design/construction industry, we need to be able to identify and address the specific needs of women in our industry, including those A/E’s who are on the facility Owner side.

This Forum will provide a venue to openly discuss the issues affecting our industry and ideas to address those issues.The program includes time for presentations and a panel discussion by accomplished women in our industry, and facilitated table and open discussions to form solutions with your peers. You will come away with ideas you can implement within your organization to build processes and a supportive culture for women

IN THE ATTACHMENTS
* you'll find our company logo

Target Market(s)

Women in the design and construction industry

Industry/Entity Type

Construction

Requirements
Must have
• Logo, event name, date, time, location, panelists names and pics, NBF continuing education provided, contact information: Maren Holtzclaw, maren.holtzclaw@c-sfpw.org, (555) 740-1938
• Register at: www.c-sfpw.org/events
• Design should encompass the description given above.
Nice to have
• Colors that compliment our logo

```html
<!DOCTYPE html>
<html lang="en">
<head>
<meta charset="utf-8">
<title>AEC Industry Women's Mini-Forum &amp; Workshop</title>
<link href="https://fonts.googleapis.com/css2?family=Oswald:wght@500;600;700&family=Open+Sans:wght@400;600;700&display=swap" rel="stylesheet">
<style>
  :root {
    --navy: #1b3a6b;
    --title-blue: #1f4e8c;
    --accent: #e8501e;
    --panel-blue: rgba(28, 104, 170, 0.88);
    --panel-green: rgba(118, 176, 64, 0.9);
    --text-dark: #243244;
    --white: #ffffff;
  }
  * { margin: 0; padding: 0; box-sizing: border-box; }
  html, body { width: 849px; height: 1200px; overflow: hidden; background: var(--white); }
  .flyer {
    position: relative; width: 849px; height: 1200px; overflow: hidden;
    background: var(--white); font-family: "Open Sans", Arial, sans-serif; color: var(--text-dark);
  }
  .brand {
    position: absolute; top: 16px; right: 26px; display: flex; flex-direction: column; align-items: flex-end;
  }
  .brand-row { display: flex; align-items: center; gap: 12px; }
  .brand-mark { width: 54px; height: 54px; border-radius: 50%; background: var(--title-blue); }
  .brand-name { font-family: "Oswald", sans-serif; font-weight: 600; font-size: 52px; color: var(--navy); line-height: 1; }
  .brand-tagline { font-size: 13px; font-weight: 600; color: var(--navy); margin-top: 6px; }

  .headline { position: absolute; top: 96px; left: 0; width: 849px; text-align: center; }
  .event-title {
    font-family: "Oswald", sans-serif; font-weight: 700; color: var(--title-blue);
    font-size: 50px; line-height: 1.02; text-transform: uppercase;
  }
  .event-date {
    font-family: "Oswald", sans-serif; font-weight: 700; color: var(--accent);
    font-size: 48px; line-height: 1.15; margin-top: 4px;
  }
  .event-venue { font-family: "Oswald", sans-serif; font-weight: 500; color: var(--navy); font-size: 27px; line-height: 1.2; }

  .hero {
    position: absolute; top: 285px; left: 0; width: 849px; height: 570px;
    background: linear-gradient(160deg, #cfe3f2 0%, #8fb3cf 35%, #5f7f99 65%, #3f566b 100%);
  }
  .intro {
    position: absolute; top: 292px; left: 104px; width: 326px; height: 500px;
    background: var(--panel-blue); color: var(--white); padding: 16px 16px;
    font-size: 12.4px; line-height: 1.34;
  }
  .intro p + p { margin-top: 6px; }
  .program {
    position: absolute; top: 590px; left: 430px; width: 419px; height: 230px;
    background: var(--panel-green); color: var(--white); padding: 12px 18px;
    font-size: 12.6px; line-height: 1.33; font-weight: 600;
  }
  .program h2 { font-family: "Oswald", sans-serif; font-size: 19px; font-weight: 600; line-height: 1.2; margin-bottom: 2px; }
  .program .program-start { font-family: "Oswald", sans-serif; font-size: 17px; font-weight: 600; }
  .program ul { list-style: none; }

  .credits {
    position: absolute; top: 870px; left: 40px; width: 769px;
    font-size: 13.4px; line-height: 1.55; text-align: center; color: var(--navy);
  }
  .credits .role { font-weight: 700; color: var(--navy); }
  .credits .name { font-weight: 600; color: var(--accent); }
  .contact {
    position: absolute; top: 985px; left: 0; width: 849px; text-align: center;
    font-size: 16px; font-weight: 600; color: var(--navy);
  }
  .contact .label { font-weight: 700; color: var(--accent); }
  .register {
    position: absolute; top: 1022px; left: 0; width: 849px; text-align: center;
    font-family: "Oswald", sans-serif; font-weight: 600; font-size: 32px; color: var(--title-blue);
  }
</style>
</head>
<body>
<main class="flyer">
  <header class="brand">
    <div class="brand-row">
      <span class="brand-mark" aria-hidden="true"></span>
      <span class="brand-name">C-SfPW</span>
    </div>
    <span class="brand-tagline">Council for Stewardship of Public Works</span>
  </header>

  <section class="headline">
    <h1 class="event-title">AEC Industry Women's<br>Mini-Forum &amp; Workshop</h1>
    <p class="event-date">JANUARY 13, 2016</p>
    <p class="event-venue">Harborview Suites, San Marcos, Texas</p>
  </section>

  <div class="hero" role="img" aria-label="Photo of professionals shaking hands in front of a city skyline"></div>

  <section class="intro">
    <p>With an increasing need for professional staffing in our design and construction industry it is important for organizations to be able to attract, support, and retain people of all genders. With the increase of women entering the design/construction industry, we need to be able to identify and address the specific needs of women in our industry, including those A/E's who are on the facility Owner side.</p>
    <p>This Forum will provide a venue to openly discuss the issues affecting our industry and ideas to address those issues.</p>
    <p>The program includes time for presentations and a panel discussion by accomplished women in our industry, and facilitated table and open discussions to form solutions with your peers. You will come away with ideas that you can implement within your organization to build processes and a supportive culture for women.</p>
    <p>&bull; Presenters and Panelists: architect, engineer, contractor, sub/trade, facility Owner<br>&bull; Table Facilitators: one for each table, with tables divided into industry segments; architects, engineers, contractors, subs/trades, Owners.</p>
    <p>A visual note-taker and separate scribe will be utilized to compile ideas and solutions, for distribution to participants after the event.</p>
  </section>

  <section class="program">
    <h2>PROGRAM TIMING:</h2>
    <ul>
      <li>1:00 Registration and Networking (refreshments)</li>
      <li class="program-start">1:30 PROGRAM:</li>
      <li>1:30 Welcome and introduce panel moderator (Dana Whitcombe)</li>
      <li>1:35 Presentations</li>
      <li>2:20 Panel/Q&amp;A</li>
      <li>3:20 Break (refreshments)</li>
      <li>3:40 Table discussions &ndash; facilitated: focus on ideas to address issues</li>
      <li>4:15 Report out and open discussion &ndash; solutions!</li>
      <li>4:40 Conclusion, Closing</li>
      <li>4:45 Adjourn</li>
    </ul>
  </section>

  <section class="credits">
    <p><span class="role">Master of Ceremonies:</span> <span class="name">Dana Whitcombe</span> &ndash; <span class="role">Scribe:</span> <span class="name">Maren Holtzclaw</span> &ndash; <span class="role">Visual Note Taking:</span> <span class="name">Priya Lindqvist</span> http://lindqvistvisuals.com/connect (??) &ndash; <span class="role">Panel:</span> Moderator &ndash; <span class="name">Teresa Ollander (Keystone Build Co.)</span></p>
    <p><span class="role">Architect:</span> <span class="name">Joan Petrakis Architects</span> &ndash; <span class="role">Engineer:</span> ?? <span class="name">Ruth Calloway</span> &ndash; <span class="role">Contractor:</span> <span class="name">Lena Marchetti (Marchetti Builders)</span></p>
    <p><span class="role">Owner:</span> <span class="name">Nadia Forsberg (State Univ. Facilities)</span> &ndash; <span class="role">Sub/trade:</span> ??</p>
  </section>

  <p class="contact"><span class="label">CONTACT :</span> Maren Holtzclaw &ndash; maren.holtzclaw@c-sfpw.org &ndash; (555) 740-1938</p>
  <p class="register">Register at: www.c-sfpw.org/events</p>
</main>
</body>
</html>
```